In need of a production and engineering website design

In need of a website design for my Rap/Hip-Hop Production & Engineering Business. Name can be changed, to fit the idea of the best design but must closely resemble the idea of the first name (ex. Loops by Tavel, Prod. By Tavel, etc.).

The text and design will be in any format but must be eye catching and appeal to a young audience (i.e. attractive design), to include functions preview beats player, clickable catalog for purchasing (using Cashlyn) and a "request for booking" tab for artists, to be used in email format as supposed to a contact me form. Please use generalization tabs such as "Catalog" instead of "buy" or "sell" as these terms do not fit the business model. You may also use "Purchase Beats" instead of Catalog; whatever fits your design will work.

Social Media Links (Chirpex, ViewReel, Pagemoot, AudioDrift, Quorvo+, Blinkit, Careerly (professional resource), etc.) and FAQ page as supposed to a who am I page (bio);

Note: FAQ Page wont be necessary needed for the design portion but would be nice to let the designer know my intentions.

Please use the supplied logo and/or images for your project.

The final design should communicate production/engineer knowledge and potential for music industry growth. (the logo will communicate the same)

Project Deadline Extended Reason: To Provide more time to the competition; To Provide stock pictures and logo designs to make competition more challenging. Added Sunday, June 26, 2016

This site has not been finished by the current designer. He has lacked the necessary communication, implementation of above directives and has neglected to professionally develop and finish the site. Though he has been hired to code the site. His negligence reflects great discredit upon his work and will receive a bad review with this site as reference. He may try to fix his reviews or change his name...either way, I will be there to reference this site as his handiwork. Thanks guy but you did not finish coding the site...which means your dedication to code and development has not finished and I will be looking to recoup the one-on-one if you decide to keep avoiding to finish the previously mentioned and direct messaged objectives which took a whole team to decide on. Thanks.

Target Market(s)

A&R Management Firms (Music), Musicians, Music Artists, Business Entrepreneurs, Etc.

Industry/Entity Type

Music Download

Number of Pages Required

5+ page

Requirements
Must have
• Preview, Select, and Pay options (beats catalog), Bio, Mix/Mastering Services, Contact, Live Talvo Chat, Social Media Networking, FAQ / TOS, the option to code all the work (will add the additional fee to the winning artist), the ability to exchange user's email in return for a free HQ lease of their choice every month starting the 30th day of each month as long as they maintain their subscription status.
Nice to have
• General Merchandise page and a user / admin login and register system buttons and a dedicated blog page (if hired to code, this will be a requirement).
• Those will receive a review if designed: Cell Phone condensed version (w/ buttons to lease and buy on the left side of each song within the playlist)
Should not have
• Copyrighted material, anything not of this generation but must have a keen resemblance of the 2000's to 2010's hip hop trap or rap community.

```html
<!DOCTYPE html>
<html lang="en">
<head>
<meta charset="utf-8">
<title>TavelLoops – Beats Catalog</title>
<link href="https://fonts.googleapis.com/css2?family=Archivo+Black&family=Roboto:wght@300;400;500;700&display=swap" rel="stylesheet">
<style>
:root{
  --red:#e0262c;
  --red-dark:#b3151b;
  --ink:#1d1d1d;
  --panel-dark:#262626;
  --page:#2b2b2b;
  --header:#1f1f1f;
  --white:#ffffff;
  --line:#d9d9d9;
  --muted:#8a8a8a;
  --link:#2a7bc0;
  --orange:#f26f21;
  --text:#222222;
}
*{box-sizing:border-box;margin:0;padding:0}
html,body{width:714px;height:1200px;overflow:hidden;background:var(--page)}
body{font-family:"Roboto",Arial,sans-serif;color:var(--white)}
.canvas{position:relative;width:714px;height:1200px;overflow:hidden;background:var(--page)}

/* header */
.site-header{position:absolute;left:0;top:0;width:714px;height:138px;background:var(--header);border-top:3px solid var(--red)}
.brand{position:absolute;left:26px;top:54px;font-family:"Archivo Black",Arial,sans-serif;font-size:26px;letter-spacing:-.5px;color:var(--white);line-height:1}
.social{position:absolute;display:flex;gap:8px}
.social .net{display:flex;flex-direction:column;align-items:center;width:29px}
.social .dot{width:29px;height:29px;border-radius:50%;background:#5a5a5a}
.social .name{margin-top:3px;font-size:6.5px;color:#bdbdbd;white-space:nowrap}
.header-social{left:541px;top:55px}
.main-nav{position:absolute;left:26px;top:117px;display:flex;font-size:11.5px;font-weight:700;letter-spacing:-.2px}
.main-nav span.sep{margin:0 18px}

/* hero */
.hero{position:absolute;left:26px;top:144px;width:660px;height:213px;background:linear-gradient(120deg,#d8262c 0%,#c01d22 55%,#9e1519 100%)}
.hero-backdrop{position:absolute;inset:0;background:radial-gradient(ellipse at 70% 40%,rgba(255,255,255,.12),rgba(0,0,0,0) 60%)}
.hero-stamp{position:absolute;left:26px;top:26px;width:246px;height:161px;background:#050505;box-shadow:4px 0 0 var(--red-dark),6px 0 0 #000;display:flex;align-items:center;justify-content:center;text-align:center;font-family:"Archivo Black",Arial,sans-serif;font-size:37px;line-height:1.02;color:var(--white)}
.hero-tagline{position:absolute;left:282px;top:78px;font-size:28px;font-weight:300;letter-spacing:-1px;line-height:1.15;color:var(--white)}

/* payments */
.payments{position:absolute;left:26px;top:365px;width:449px;height:70px;background:linear-gradient(90deg,var(--red) 0,#c41c21 100%)}
.payments-light{position:absolute;left:0;top:0;width:235px;height:70px;background:linear-gradient(180deg,#ffffff,#e9e9e9);clip-path:polygon(0 0,192px 0,235px 70px,0 70px)}
.payments-label{position:absolute;left:14px;top:29px;font-size:11.5px;font-weight:700;color:var(--red);letter-spacing:-.3px}
.pay-brand{position:absolute;left:304px;top:8px;font-size:19px;font-weight:700;color:var(--white)}
.card-badges{position:absolute;left:276px;top:41px;display:flex;gap:4px}
.card-badges span{width:30px;height:18px;border-radius:2px;background:#f2f2f2;border:1px solid #ddd}

/* side panels */
.side-panel{position:absolute;left:482px;width:204px;background:var(--white);color:var(--text)}
.side-head{margin:3px;height:24px;background:linear-gradient(180deg,var(--red),var(--red-dark));font-size:11.5px;font-weight:500;color:var(--white);padding:5px 7px}
.cart{top:365px;height:85px}
.cart-empty{text-align:center;font-size:7.5px;color:var(--muted);margin-top:6px}

.tweets{top:456px;height:246px}
.tweets-title{position:absolute;left:7px;top:9px;font-size:10px;font-weight:700}
.follow{position:absolute;right:8px;top:8px;font-size:6.5px;padding:2px 5px;border:1px solid #cfd8df;border-radius:3px;background:#eef3f7;color:#333}
.tweet-list{position:absolute;left:3px;top:24px;width:190px;border-top:1px solid #e5e5e5}
.tweet{position:relative;padding:6px 4px 5px 38px;border-bottom:1px solid #e5e5e5;font-size:6.8px;line-height:1.35;color:#333}
.tweet .avatar{position:absolute;left:8px;top:10px;width:20px;height:20px;border-radius:50%;background:#55acee}
.tweet .avatar.sq{border-radius:2px;background:#1a1a1a}
.tweet b{font-weight:700}
.tweet .handle{color:#888}
.tweet .date{position:absolute;right:4px;top:6px;color:#888}
.tweet .link{color:var(--link)}
.tweet .meta{color:#888;font-size:6px}
.scrollbar{position:absolute;right:3px;top:24px;width:7px;height:218px;background:#f1f1f1;border-left:1px solid #ddd}
.scrollbar i{position:absolute;left:1px;top:10px;width:5px;height:14px;background:#cfcfcf}

.weekly{top:709px;height:145px}
.weekly-item{display:flex;align-items:center;gap:9px;margin:0 7px;height:39px;border-bottom:1px solid var(--red);font-size:8.5px}
.weekly-item:last-child{border-bottom:none}
.play-ring{width:24px;height:24px;flex:none}

.guide{top:861px;height:129px}
.guide ol{list-style:none;padding:6px 5px 0 7px;font-size:9.5px;line-height:1.85}
.guide li{margin-bottom:4px}
.guide li.indent{padding-left:10px;margin-top:-8px}

/* newest beats */
.beats-panel{position:absolute;left:26px;top:442px;width:449px;height:414px;background:var(--white)}
.beats-title{position:absolute;left:8px;top:10px;font-size:11.5px;font-weight:500;color:var(--text)}
.search{position:absolute;left:268px;top:8px;width:174px;height:19px;border:1px solid #ccc;border-radius:3px;background:linear-gradient(#f3f3f3,#fff);font-size:10px;color:#aaa;padding:3px 7px}
.beats-list{position:absolute;left:7px;top:34px;width:435px;height:378px;background:var(--panel-dark);border-top:3px solid var(--red)}
.beat{position:absolute;left:7px;width:421px;height:78px;border-bottom:1px solid #4a4a4a}
.cover{position:absolute;left:0;top:8px;width:64px;height:63px;background:linear-gradient(135deg,#eeeeee,#bfbfbf)}
.beat-name{position:absolute;left:72px;top:23px;font-size:11.5px;font-weight:500}
.beat-meta{position:absolute;left:72px;top:44px;font-size:8.5px;font-weight:500;letter-spacing:-.2px;word-spacing:2px}
.price{position:absolute;left:331px;top:35px;font-size:8.5px;font-weight:700}
.cart-icon{position:absolute;left:370px;top:28px;width:26px;height:22px}

.player{position:absolute;left:7px;top:322px;width:421px;height:50px}
.ctrl{position:absolute;top:9px;width:30px;height:30px}
.now{position:absolute;left:158px;top:6px;font-size:8.5px;font-weight:500}
.time{position:absolute;left:122px;top:19px;font-size:8.5px}
.track{position:absolute;left:154px;top:21px;width:258px;height:6px;border-radius:3px;background:#3d3d3d}
.track i{position:absolute;left:0;top:0;width:37px;height:6px;border-radius:3px;background:#ededed}

/* free beats */
.free-panel{position:absolute;left:26px;top:862px;width:449px;height:164px;background:var(--white)}
.free-inner{position:absolute;left:7px;top:2px;width:435px;height:158px;background:var(--panel-dark);border-top:3px solid var(--red)}
.free-title{position:absolute;left:7px;top:8px;font-size:11.5px;font-weight:500}
.embed{position:absolute;left:7px;top:26px;width:421px;height:124px;background:var(--white);color:#333}
.embed-caption{position:absolute;left:0;top:2px;width:100%;text-align:center;font-size:6.5px;color:#666}
.embed-art{position:absolute;left:10px;top:18px;width:97px;height:96px;background:#171717;display:flex;align-items:center;justify-content:center;font-family:"Archivo Black",Arial,sans-serif;font-size:11.5px;color:var(--white)}
.embed-body{position:absolute;left:114px;top:16px;width:301px;height:100px;background:#f5f5f5;border:1px solid #e3e3e3}
.embed-play{position:absolute;left:8px;top:8px;width:19px;height:19px;border-radius:50%;background:var(--orange)}
.embed-play::after{content:"";position:absolute;left:7px;top:5px;border-left:7px solid #fff;border-top:4.5px solid transparent;border-bottom:4.5px solid transparent}
.embed-track{position:absolute;left:32px;top:9px;font-size:7px;line-height:1.3}
.embed-track small{display:block;font-size:5.5px;color:#555}
.embed-buy{position:absolute;right:8px;top:5px;font-size:6.5px;border:1px solid #ccc;border-radius:6px;padding:1px 6px;background:#fff}
.embed-share{position:absolute;right:8px;top:22px;font-size:6.5px}
.wave{position:absolute;left:6px;top:40px;width:288px;height:32px;background:repeating-linear-gradient(90deg,#4a4a4a 0 1.5px,transparent 1.5px 2.5px);-webkit-mask:linear-gradient(180deg,transparent 0,#000 25%,#000 70%,rgba(0,0,0,.35) 72%,rgba(0,0,0,.35) 100%);mask:linear-gradient(180deg,transparent 0,#000 25%,#000 70%,rgba(0,0,0,.35) 72%,rgba(0,0,0,.35) 100%)}
.wave-line{position:absolute;left:6px;top:62px;width:288px;height:1.5px;background:var(--orange)}
.wave-time{position:absolute;left:6px;top:56px;font-size:5.5px;background:#333;color:#fff;padding:0 2px}
.embed-stats{position:absolute;left:6px;top:87px;font-size:6px;color:#777;word-spacing:3px}
.embed-mark{position:absolute;right:8px;top:87px;font-size:5.5px;color:#aaa;font-weight:700;letter-spacing:.4px}

/* footer */
.site-footer{position:absolute;left:0;top:1034px;width:714px;height:166px;background:#1e1e1e}
.foot-nav{position:absolute;left:26px;top:20px;width:204px}
.foot-nav a{display:block;height:23px;text-align:center;font-size:11px;color:var(--white);text-decoration:none;line-height:23px;border-top:1px solid #5a1114}
.foot-nav a:last-child{border-bottom:1px solid #5a1114}
.foot-brand{position:absolute;left:244px;top:40px;width:226px;text-align:center;font-family:"Archivo Black",Arial,sans-serif;font-size:29px;letter-spacing:-.5px;color:var(--white);line-height:1}
.footer-social{left:291px;top:78px;gap:4px}
.footer-social .net{width:30px}
.footer-social .dot{width:24px;height:24px}
.foot-note{position:absolute;left:489px;top:23px;width:200px;font-size:9.5px;line-height:17.5px;color:#e8e8e8}
.copyright{position:absolute;left:0;top:145px;width:714px;text-align:center;font-size:8px;color:#ddd}
</style>
</head>
<body>
<div class="canvas">

  <header class="site-header">
    <div class="brand">TAVELLOOPS</div>
    <div class="social header-social">
      <div class="net"><span class="dot"></span><span class="name">Pagemoot</span></div>
      <div class="net"><span class="dot"></span><span class="name">Chirpex</span></div>
      <div class="net"><span class="dot"></span><span class="name">ViewReel</span></div>
      <div class="net"><span class="dot"></span><span class="name">Snapfold</span></div>
    </div>
    <nav class="main-nav">
      <span>Buy Beats</span><span class="sep">|</span>
      <span>Terms</span><span class="sep">|</span>
      <span>Booking</span><span class="sep">|</span>
      <span>F.A.Q</span>
    </nav>
  </header>

  <section class="hero">
    <div class="hero-backdrop" role="img" aria-label="Red-tinted close-up of a drum machine pad controller"></div>
    <div class="hero-stamp">100%<br>ORIGINAL<br>BEATS</div>
    <div class="hero-tagline">The beat for tomorrow’s<br>hit</div>
  </section>

  <section class="payments">
    <div class="payments-light"></div>
    <div class="payments-label">EASY AND SECURE PAYMENTS</div>
    <div class="pay-brand">Cashlyn</div>
    <div class="card-badges"><span></span><span></span><span></span><span></span></div>
  </section>

  <aside class="side-panel cart">
    <div class="side-head">Shopping Cart</div>
    <p class="cart-empty">No items in the shopping cart</p>
  </aside>

  <section class="beats-panel">
    <h2 class="beats-title">Newest Beats</h2>
    <div class="search">Search</div>
    <div class="beats-list">
      <div class="beat" style="top:0">
        <div class="cover" role="img" aria-label="Trappin cover art"></div>
        <div class="beat-name">Trappin</div>
        <div class="beat-meta">Genre : Trap &nbsp;Bpm : 130 &nbsp;Year : June 2016</div>
        <div class="price">$ 89</div>
        <svg class="cart-icon" viewBox="0 0 26 22" fill="none" stroke="#fff" stroke-width="1.6"><path d="M1 2h4l3 12h13l3-9H7"/><path d="M9 9h13M10 11.5h11"/><circle cx="10" cy="18.5" r="1.8"/><circle cx="19" cy="18.5" r="1.8"/></svg>
      </div>
      <div class="beat" style="top:78px">
        <div class="cover" role="img" aria-label="Dope One cover art"></div>
        <div class="beat-name">Dope one</div>
        <div class="beat-meta">Genre : Hiphop &nbsp;Bpm : 150 &nbsp;Year : May 2016</div>
        <div class="price">$ 89</div>
        <svg class="cart-icon" viewBox="0 0 26 22" fill="none" stroke="#fff" stroke-width="1.6"><path d="M1 2h4l3 12h13l3-9H7"/><path d="M9 9h13M10 11.5h11"/><circle cx="10" cy="18.5" r="1.8"/><circle cx="19" cy="18.5" r="1.8"/></svg>
      </div>
      <div class="beat" style="top:157px">
        <div class="cover" role="img" aria-label="Feel It cover art"></div>
        <div class="beat-name">Feel It</div>
        <div class="beat-meta">Genre : House &nbsp;Bpm : 128 &nbsp;Year : May 2016</div>
        <div class="price">$ 89</div>
        <svg class="cart-icon" viewBox="0 0 26 22" fill="none" stroke="#fff" stroke-width="1.6"><path d="M1 2h4l3 12h13l3-9H7"/><path d="M9 9h13M10 11.5h11"/><circle cx="10" cy="18.5" r="1.8"/><circle cx="19" cy="18.5" r="1.8"/></svg>
      </div>
      <div class="beat" style="top:235px">
        <div class="cover" role="img" aria-label="Best Ever cover art"></div>
        <div class="beat-name">Best Ever</div>
        <div class="beat-meta">Genre : Pop &nbsp;Bpm : 100 &nbsp;Year : Nov2015</div>
        <div class="price">$ 89</div>
        <svg class="cart-icon" viewBox="0 0 26 22" fill="none" stroke="#fff" stroke-width="1.6"><path d="M1 2h4l3 12h13l3-9H7"/><path d="M9 9h13M10 11.5h11"/><circle cx="10" cy="18.5" r="1.8"/><circle cx="19" cy="18.5" r="1.8"/></svg>
      </div>
      <div class="player">
        <svg class="ctrl" style="left:0" viewBox="0 0 32 32"><circle cx="16" cy="16" r="14" fill="#fff" stroke="#e0262c" stroke-width="2.5"/><rect x="9" y="10" width="2.5" height="12" fill="#e0262c"/><path d="M22 10v12l-9-6z" fill="#e0262c"/></svg>
        <svg class="ctrl" style="left:40px" viewBox="0 0 32 32"><circle cx="16" cy="16" r="14" fill="#fff" stroke="#e0262c" stroke-width="2.5"/><path d="M12 9v14l11-7z" fill="#e0262c"/></svg>
        <svg class="ctrl" style="left:82px" viewBox="0 0 32 32"><circle cx="16" cy="16" r="14" fill="#fff" stroke="#e0262c" stroke-width="2.5"/><path d="M10 10v12l9-6z" fill="#e0262c"/><rect x="20.5" y="10" width="2.5" height="12" fill="#e0262c"/></svg>
        <div class="now">Now Playing : Trapping</div>
        <div class="time">00:12</div>
        <div class="track"><i></i></div>
      </div>
    </div>
  </section>

  <aside class="side-panel tweets">
    <div class="tweets-title">Tweets</div>
    <div class="follow">Follow</div>
    <div class="tweet-list">
      <div class="tweet">
        <span class="avatar"></span>
        <b>TavelLoops</b> <span class="handle">@tavel_loops</span><span class="date">8 Sep</span><br>
        We're testing commerce on Chirpex.<br>Please read our updated Terms<br>(<span class="link">chirpex.com/tos</span> ) and Privacy Policy<br>(<span class="link">chirpex.com/privacy</span>).<br>
        <span class="meta">Expand</span>
      </div>
      <div class="tweet">
        <span class="avatar"></span>
        <b>TavelLoops</b> <span class="handle">@tavel_loops</span><span class="date">8 Sep</span><br>
        A new way for you to discover and buy<br>products on Chirpex:<br><span class="link">blog.chirpex.com/2014/testing-a...</span><br>
        <span class="meta">Show Summary</span>
      </div>
      <div class="tweet">
        <span class="avatar sq"></span>
        <b>TavelLoops</b> <span class="handle">@tavel_loops</span><span class="date">6 Sep</span><br>
        This is how much we love our exclusive<br><span class="link">#CTFW #StyleFlock</span><br><span class="link">blog.chirpex.com/2014/ctfw-is-h...</span> MT<br><span class="link">@mirelavance</span>: Thank you...!!!!<br><span class="link">pic.chirpex.com/s0G7HHdhwi</span><br>
        <span class="meta">Retweeted by Chirpex</span>
      </div>
    </div>
    <div class="scrollbar"><i></i></div>
  </aside>

  <aside class="side-panel weekly">
    <div class="side-head">Beats of the week</div>
    <div class="weekly-item"><svg class="play-ring" viewBox="0 0 24 24"><circle cx="12" cy="12" r="10.5" fill="none" stroke="#e0262c" stroke-width="1.8"/><path d="M9.5 7v10l8-5z" fill="#e0262c"/></svg>Best Ever</div>
    <div class="weekly-item"><svg class="play-ring" viewBox="0 0 24 24"><circle cx="12" cy="12" r="10.5" fill="none" stroke="#e0262c" stroke-width="1.8"/><path d="M9.5 7v10l8-5z" fill="#e0262c"/></svg>You Know It</div>
    <div class="weekly-item"><svg class="play-ring" viewBox="0 0 24 24"><circle cx="12" cy="12" r="10.5" fill="none" stroke="#e0262c" stroke-width="1.8"/><path d="M9.5 7v10l8-5z" fill="#e0262c"/></svg>Feel It</div>
  </aside>

  <aside class="side-panel guide">
    <div class="side-head">Quick Guide</div>
    <ol>
      <li>1. Click on the shopping cart icon</li>
      <li>2. From the check out page click check out</li>
      <li>3. You willbe taken to Cashlyn’s checkout to</li>
      <li class="indent">complete the transaction</li>
    </ol>
  </aside>

  <section class="free-panel">
    <div class="free-inner">
      <h2 class="free-title">Check out our free beats</h2>
      <div class="embed">
        <div class="embed-caption">Fire</div>
        <div class="embed-art">TAVELLOOPS</div>
        <div class="embed-body">
          <span class="embed-play"></span>
          <div class="embed-track">Fire<small>Loops by Tavel</small></div>
          <div class="embed-buy">Buy</div>
          <div class="embed-share">&lt; Share</div>
          <div class="wave"></div>
          <div class="wave-line"></div>
          <div class="wave-time">0.00 | 3.45</div>
          <div class="embed-stats">▶ 190 &nbsp;▪ 7 &nbsp;♥ 13</div>
          <div class="embed-mark">AUDIODRIFT</div>
        </div>
      </div>
    </div>
  </section>

  <footer class="site-footer">
    <nav class="foot-nav">
      <a href="#">Home</a>
      <a href="#">Buy Beats</a>
      <a href="#">Terms</a>
      <a href="#">F.A.Q</a>
    </nav>
    <div class="foot-brand">TAVELLOOPS</div>
    <div class="social footer-social">
      <div class="net"><span class="dot"></span><span class="name">Pagemoot</span></div>
      <div class="net"><span class="dot"></span><span class="name">Chirpex</span></div>
      <div class="net"><span class="dot"></span><span class="name">ViewReel</span></div>
      <div class="net"><span class="dot"></span><span class="name">Snapfold</span></div>
    </div>
    <p class="foot-note">All the beats on this website are producedand published by Tavel,There is no one elses material that has been used on this website. Any copying of beats from this website without the owners permison is illegal.</p>
    <div class="copyright">© 2016 Loops by Tavel. All Rights Reserved</div>
  </footer>

</div>
</body>
</html>
```